Marwen + Dobbs Chocolate Cafe - Takeaway Packaging

Packaging Design required for premium chocolate cafe brand

1. 8 oz & 12 oz takeaway cups - ideally logo in gold foil - innovative luxury / premium look - designed to fit the same lid on both cup size.
2. Paper bag range for chocolate products - two sizes (180mm(w) x 90mm(d) x280mm(h)) & (360mm (w) x 120mm (d) x 310mm (h)).
3. Paper napkins - 15cm square cocktail napkin
4. Branded Greaseproof paper wrap for sandwiches
5. Branded Greaseproof Baking Paper for muffins
6. Branded Takeaway Cake boxes
7. Branded Greaseproof paper loose chocolate bags - two sizes (100mm (w) x 30mm (d) x 195mm (h) and (100mm (w) x 30mm (d) x 100mm (h))

See detailed brand guidelines and logo samples attached.
Happy for alternative Colour scheme proposals - other than colours set out in brand guidelines.

Detailed M+D Takeaway Cup brief & Paperbag Briefs attached.

Target Market(s)

Premium Retail / Cafe

Industry/Entity Type

Chocolate Retail / Cafe

Font styles to use
Other font styles liked:
• Raleway Light, LATO Clean & Trajan Pro Bold

Requirements
Must have
• Scandi, Modern, Premium, Luxury feel & design
Nice to have
• Logo in Gold foil

```html
<!DOCTYPE html>
<html lang="en">
<head>
<meta charset="utf-8">
<title>Marwen + Dobbs Chocolate Cafe – Bag Panel</title>
<link rel="stylesheet" href="https://fonts.googleapis.com/css2?family=Raleway:wght@500;600&display=swap">
<style>
  :root {
    --backdrop: #eaf1ea;
    --panel-mint: #d8e6da;
    --panel-black: #120e0a;
    --gold: #c9973a;
    --gold-light: #f6dc84;
    --gold-deep: #b07a22;
    --ink: #1a1a1a;
  }
  html, body {
    margin: 0;
    width: 1200px;
    height: 1200px;
    overflow: hidden;
    background: var(--backdrop);
  }
  .canvas {
    position: relative;
    width: 1200px;
    height: 1200px;
  }
  .bag-panel {
    position: absolute;
    left: 455px;
    top: 100px;
    width: 290px;
    height: 1000px;
    border-radius: 12px;
    overflow: hidden;
    background: var(--panel-mint);
    font-family: "Raleway", sans-serif;
  }
  .brand-block {
    position: absolute;
    left: 0;
    top: 0;
    width: 100%;
    height: 347px;
    background: var(--panel-black);
  }
  .brand-name {
    position: absolute;
    left: 20px;
    right: 20px;
    top: 150px;
    margin: 0;
    text-align: center;
    color: var(--gold);
    font-weight: 600;
    font-size: 19px;
    line-height: 1.45;
    letter-spacing: 0.1em;
    text-transform: uppercase;
  }
  .product-line {
    position: absolute;
    left: 0;
    right: 0;
    top: 272px;
    margin: 0;
    text-align: center;
    color: var(--gold);
    font-weight: 500;
    font-size: 13px;
    letter-spacing: 0.12em;
    text-transform: uppercase;
  }
  .gold-band {
    position: absolute;
    left: 0;
    top: 347px;
    width: 100%;
    height: 13px;
    background: linear-gradient(90deg, var(--gold-deep) 0%, var(--gold-light) 22%, var(--gold) 55%, var(--gold-deep) 80%, #e1b24a 100%);
  }
  .tagline {
    position: absolute;
    left: 0;
    right: 0;
    top: 646px;
    margin: 0;
    text-align: center;
    color: var(--ink);
    font-weight: 500;
    font-size: 14px;
    letter-spacing: 0.14em;
    text-transform: uppercase;
  }
</style>
</head>
<body>
  <main class="canvas">
    <section class="bag-panel">
      <div class="brand-block">
        <h1 class="brand-name">Marwen + Dobbs Chocolate Cafe</h1>
        <p class="product-line">Luxury Chocolates</p>
      </div>
      <div class="gold-band"></div>
      <p class="tagline">Crafted to Delight</p>
    </section>
  </main>
</body>
</html>
```